full stationary design for a modern sleek design company

we are a design company that does modern minimalistic interior design works as well as other design services for high end clients.
we need a full stationary design including and not limited to (double sided business card, letter head, envelopes, documents folder...etc) that reflects the modern style design we do.
sleek modern and minimalistic is the requirements.
Updates

please use the latest attached files as there was a slight modification on the logo Added Wednesday, March 1, 2017

minor update on the logo files in JPG and PSD has been updated kindly follow the new attachments. Added Thursday, March 2, 2017

Target Market(s)

modern minimalist clients

Industry/Entity Type

Design Agency

Requirements
Must have
• the logo
Nice to have
• i like the colors in the colored 3D logo attached
Should not have
• too many colors

```html
<!DOCTYPE html>
<html lang="en">
<head>
<meta charset="utf-8">
<title>Linea Studio – Stationery Set</title>
<link href="https://fonts.googleapis.com/css2?family=Montserrat:wght@500;600&family=Open+Sans:wght@400;600&display=swap" rel="stylesheet">
<style>
  :root {
    --orange: #e3922c;
    --charcoal: #3b3b3b;
    --paper: #fbfbfb;
    --backdrop: #ececec;
    --ink: #555555;
    --light-text: #f2f2f2;
  }
  * { box-sizing: border-box; margin: 0; padding: 0; }
  html, body { width: 1200px; height: 903px; overflow: hidden; }
  body {
    position: relative;
    background: var(--backdrop);
    font-family: "Open Sans", Arial, sans-serif;
    color: var(--ink);
  }
  .piece { position: absolute; background: var(--paper); }

  /* brand mark: square + name */
  .brand {
    display: flex; align-items: center;
    font-family: "Montserrat", Arial, sans-serif;
    font-weight: 600; letter-spacing: 0.06em; text-transform: uppercase;
    white-space: nowrap;
  }
  .brand-square { background: var(--orange); flex: none; }
  .brand-name { color: var(--charcoal); }
  .brand.on-dark .brand-name { color: var(--light-text); }

  /* letterhead */
  .letterhead { left: 187px; top: 63px; width: 371px; height: 523px; border-top: 6px solid var(--orange); border-bottom: 6px solid var(--charcoal); }
  .letterhead .brand { position: absolute; top: 34px; left: 0; right: 0; justify-content: center; font-size: 11px; gap: 6px; }
  .letterhead .brand-square { width: 12px; height: 12px; }
  .letterhead-footer { position: absolute; left: 22px; right: 22px; bottom: 14px; }
  .footer-rule { position: relative; height: 1px; background: #9a9a9a; margin-bottom: 7px; }
  .footer-icon { position: absolute; top: -4px; width: 9px; height: 9px; background: var(--orange); }
  .footer-icon svg { display: block; width: 9px; height: 9px; }
  .footer-cols { display: flex; justify-content: space-between; font-size: 5px; line-height: 1.5; color: var(--ink); }
  .footer-cols .right { text-align: right; }
  .footer-cols .center { text-align: center; }

  /* folder */
  .folder { left: 620px; top: 38px; width: 440px; height: 554px; background: var(--charcoal); }
  .folder-spine { position: absolute; left: 0; top: 0; bottom: 0; width: 28px; background: var(--orange); }
  .folder .brand { position: absolute; left: 66px; top: 292px; font-size: 26px; gap: 14px; }
  .folder .brand-square { width: 30px; height: 30px; }

  /* business cards */
  .card-front { left: 54px; top: 627px; width: 169px; height: 93px; }
  .card-front .brand { position: absolute; left: 8px; top: 43px; font-size: 6.5px; gap: 4px; }
  .card-front .brand-square { width: 7px; height: 7px; }
  .card-details { position: absolute; left: 94px; top: 22px; font-size: 4.3px; line-height: 1.55; border-left: 1px solid #cfcfcf; padding-left: 5px; }
  .card-name { color: var(--orange); font-weight: 600; font-size: 5.6px; }
  .card-back { left: 54px; top: 748px; width: 169px; height: 102px; background: var(--charcoal); }
  .card-back .brand { position: absolute; left: 16px; top: 44px; font-size: 9px; gap: 6px; }
  .card-back .brand-square { width: 11px; height: 11px; }

  /* DL letter / envelope front */
  .envelope-front { left: 265px; top: 641px; width: 415px; height: 204px; border-top: 5px solid var(--orange); border-bottom: 7px solid var(--charcoal); }
  .envelope-front .brand { position: absolute; left: 14px; top: 18px; font-size: 10px; gap: 5px; }
  .envelope-front .brand-square { width: 11px; height: 11px; }
  .envelope-address { position: absolute; left: 14px; top: 37px; font-size: 5.5px; color: var(--ink); }

  /* envelope back */
  .envelope-back { left: 720px; top: 648px; width: 416px; height: 197px; }
  .envelope-flap { position: absolute; left: 0; top: 0; width: 100%; height: 70px; background: var(--charcoal); }
  .envelope-back .brand { position: absolute; left: 0; right: 0; top: 20px; justify-content: center; font-size: 11px; gap: 6px; }
  .envelope-back .brand-square { width: 12px; height: 12px; }
</style>
</head>
<body>

  <section class="piece letterhead" aria-label="Letterhead">
    <div class="brand"><span class="brand-square"></span><span class="brand-name">Linea Studio</span></div>
    <footer class="letterhead-footer">
      <div class="footer-rule">
        <span class="footer-icon" style="left:46px">
          <svg viewBox="0 0 10 10"><path d="M5 2a2 2 0 0 1 2 2c0 1.5-2 4-2 4S3 5.5 3 4a2 2 0 0 1 2-2z" fill="#fff"/></svg>
        </span>
        <span class="footer-icon" style="left:159px">
          <svg viewBox="0 0 10 10"><path d="M3 2h1.3l.6 1.6-.8.6a4 4 0 0 0 1.7 1.7l.6-.8 1.6.6V7a1 1 0 0 1-1 1A5 5 0 0 1 2 3a1 1 0 0 1 1-1z" fill="#fff"/></svg>
        </span>
        <span class="footer-icon" style="right:8px">
          <svg viewBox="0 0 10 10"><rect x="2" y="3" width="6" height="4" fill="#fff"/><path d="M2 3l3 2.2L8 3" stroke="#e3922c" stroke-width=".6" fill="none"/></svg>
        </span>
      </div>
      <div class="footer-cols">
        <p>4120 Larch Avenue<br>Juneau, Alaska 99801</p>
        <p class="center">(555) 214 8830<br>(555) 306 4471</p>
        <p class="right">adam@lineastudio.com<br>www.lineastudio.com</p>
      </div>
    </footer>
  </section>

  <section class="piece folder" aria-label="Document folder">
    <div class="folder-spine"></div>
    <div class="brand on-dark"><span class="brand-square"></span><span class="brand-name">Linea Studio</span></div>
  </section>

  <section class="piece card-front" aria-label="Business card, front">
    <div class="brand"><span class="brand-square"></span><span class="brand-name">Linea Studio</span></div>
    <div class="card-details">
      <p class="card-name">ADAM ROWE</p>
      <p>CEO &amp; Founder</p>
      <p>4120 Larch Avenue<br>Juneau, Alaska 99801</p>
      <p>(555) 214 8830</p>
      <p>(555) 306 4471</p>
      <p>adam@lineastudio.com</p>
      <p>www.lineastudio.com</p>
    </div>
  </section>

  <section class="piece card-back" aria-label="Business card, back">
    <div class="brand on-dark"><span class="brand-square"></span><span class="brand-name">Linea Studio</span></div>
  </section>

  <section class="piece envelope-front" aria-label="Envelope, front">
    <div class="brand"><span class="brand-square"></span><span class="brand-name">Linea Studio</span></div>
    <p class="envelope-address">4120 Larch Avenue, Juneau, Alaska 99801</p>
  </section>

  <section class="piece envelope-back" aria-label="Envelope, back">
    <div class="envelope-flap"></div>
    <div class="brand on-dark"><span class="brand-square"></span><span class="brand-name">Linea Studio</span></div>
  </section>

</body>
</html>
```